Vantorly Fitness - Personal & Rehab Training

Business Card for my personal training business - Vantorly Fitness. I focus on personal and rehab training. I would like a double sided card, round edges. front of card will be my existing logo and the back will have an image (black and white or exercise, people exercising, weights, etc) along with my name and details. Such as:
Calisse Dunmore
Personal & Rehab Trainer
www.vantorlyfitness-demo.com.au
0439582064
I have some images that I have downloaded that I am happy to send to the designer.
Thanks
Target Market(s)
athletes, middle to high income, sport related
Contact Information for Business Card
Calisse Dunmore
Personal & Rehab Trainer
0439582064
Colors
Designer to choose only greyscale colors for use in the design.
Requirements
Must have
- my existing logo
Nice to have
- one of the images uploaded. I really like the girl with the mint coloured shoes as this is one of my logo colours

```html
<!DOCTYPE html>
<html lang="en">
<head>
<meta charset="utf-8">
<title>Vantorly Fitness – Business Card</title>
<link rel="stylesheet" href="https://fonts.googleapis.com/css2?family=Montserrat:wght@600;800&family=Libre+Baskerville&display=swap">
<style>
  :root {
    --backdrop: #2b2b2b;
    --ink: #111111;
    --paper: #ffffff;
    --ghost: #ececec;
    --photo-dark: #151515;
    --photo-mid: #5a5a5a;
    --mint: #4fd3cf;
    --white: #ffffff;
  }
  * { box-sizing: border-box; margin: 0; padding: 0; }
  html, body {
    width: 1200px; height: 880px; overflow: hidden;
    background: var(--backdrop);
  }
  .card {
    position: absolute;
    left: 290px;
    width: 620px; height: 354px;
    border-radius: 24px;
    overflow: hidden;
  }
  .card--front { top: 48px; }
  .card--back { top: 478px; background: var(--paper); }

  .photo {
    position: absolute; inset: 0;
    background:
      radial-gradient(ellipse 90px 60px at 14% 82%, rgba(79,211,207,.55), transparent 70%),
      radial-gradient(ellipse 90px 60px at 86% 22%, rgba(79,211,207,.55), transparent 70%),
      radial-gradient(ellipse 140px 120px at 58% 62%, #0a0a0a, transparent 75%),
      linear-gradient(135deg, var(--photo-mid), var(--photo-dark) 70%);
  }

  .brand {
    position: absolute;
    display: flex; align-items: center; gap: 18px;
  }
  .brand__square {
    width: 62px; height: 62px;
    border: 5px solid currentColor;
    border-radius: 10px;
  }
  .brand__name {
    font-family: "Montserrat", sans-serif;
    font-weight: 600;
    font-size: 40px;
    letter-spacing: 5px;
    text-transform: uppercase;
    line-height: 1;
  }
  .card--front .brand { left: 150px; top: 150px; color: var(--white); }
  .card--back .brand { left: 44px; top: 58px; color: var(--ink); }

  .ghost-square {
    position: absolute;
    right: -40px; top: 50px;
    width: 280px; height: 280px;
    border: 26px solid var(--ghost);
    border-radius: 40px;
  }

  .contact {
    position: absolute; left: 48px; top: 188px;
    color: var(--ink);
  }
  .contact__name {
    font-family: "Montserrat", sans-serif;
    font-weight: 800;
    font-size: 22px;
    letter-spacing: .5px;
    text-transform: uppercase;
  }
  .contact__role {
    font-family: "Libre Baskerville", serif;
    font-size: 16px;
    margin-top: 2px;
  }
  .contact__list { list-style: none; margin-top: 16px; }
  .contact__item {
    display: flex; align-items: center; gap: 10px;
    font-family: "Libre Baskerville", serif;
    font-size: 15px;
    line-height: 26px;
  }
  .contact__icon { width: 14px; height: 14px; flex: none; }
</style>
</head>
<body>
  <section class="card card--front">
    <div class="photo" role="img" aria-label="Black and white photo of a person lifting a kettlebell in a gym, wearing mint coloured shoes"></div>
    <div class="brand">
      <span class="brand__square"></span>
      <span class="brand__name">Vantorly Fitness</span>
    </div>
  </section>

  <section class="card card--back">
    <div class="ghost-square"></div>
    <div class="brand">
      <span class="brand__square"></span>
      <span class="brand__name">Vantorly Fitness</span>
    </div>
    <div class="contact">
      <p class="contact__name">Calisse Dunmore</p>
      <p class="contact__role">Personal &amp; Rehab Trainer</p>
      <ul class="contact__list">
        <li class="contact__item">
          <svg class="contact__icon" viewBox="0 0 16 16"><path fill="#111" d="M3 1l3 3-1.5 2a9 9 0 005.5 5.5L12 10l3 3-2 2C7 15 1 9 1 3z"/></svg>
          0439582064
        </li>
        <li class="contact__item">
          <svg class="contact__icon" viewBox="0 0 16 16"><rect x="1" y="3" width="14" height="10" fill="#111"/><path d="M1 3l7 6 7-6" fill="none" stroke="#fff" stroke-width="1.4"/></svg>
          info@vantorlymail-demo.com
        </li>
        <li class="contact__item">
          <svg class="contact__icon" viewBox="0 0 16 16"><circle cx="8" cy="8" r="7" fill="#111"/><path d="M1 8h14M8 1c-3 4-3 10 0 14M8 1c3 4 3 10 0 14" fill="none" stroke="#fff" stroke-width=".9"/></svg>
          www.vantorlyfitness-demo.com.au
        </li>
      </ul>
    </div>
  </section>
</body>
</html>
```